Chinese Artwork Gallery and Tea House need website design

This is a challenging website design, as the styles combines contemporary layout infused with oriental artwork style. Our company run a oriental gallery/tea house from Sydney, specialising selling oriental antique replicate such as terra-cotta warriors, porcelain vases, bronze cups, traditional Chinese painting and calligraphy, tea and tea sets. The colour scheme will incorporate the existing gold, red and black being used for our logo.

Please include in the homepage a section with large sliding image to showcase individual antique pieces, as well as image to link to 6 categories of products we are selling in retail store and online store which are Porcelain, Bronze, Terra Cotta, Painting and Calligraphy, Chinese Artwork, Tea & Tea Sets. The home page needs to highlight our brand and the design pattern we have included in the logo design. Colour wise, red, black, gold and white. I hope above helps.

```html
<!DOCTYPE html>
<html lang="en">
<head>
<meta charset="utf-8">
<title>YUNTAO – Chinese Artwork Gallery &amp; Tea House</title>
<link rel="stylesheet" href="https://fonts.googleapis.com/css2?family=Bebas+Neue&family=Arimo:wght@400;700&display=swap">
<style>
:root{
  --red:#8c0a0a;
  --red-dark:#6a0000;
  --red-price:#a30f0f;
  --gold:#f4a300;
  --white:#ffffff;
  --text:#666666;
  --text-dark:#333333;
  --line:#e2e2e2;
  --card-line:#e6e6e6;
  --footer:#161616;
}
*{margin:0;padding:0;box-sizing:border-box}
html,body{width:1200px;height:2187px;overflow:hidden;background:var(--white)}
body{position:relative;font-family:"Arimo",Arial,sans-serif;color:var(--text)}
.abs{position:absolute}
.display{font-family:"Bebas Neue",Impact,sans-serif;font-weight:400}

/* header */
.site-header{left:0;top:0;width:1200px;height:114px;background:linear-gradient(#9a0b0b,var(--red-dark));border-bottom:3px solid #5a0000}
.brand{left:131px;top:44px;font-size:22px;letter-spacing:3px;color:var(--white);font-weight:400}
.search{left:765px;top:18px;width:304px;height:33px;border:1px solid #b44;background:#7a0000;color:#e8c9c9;font-size:11px;padding:9px 0 0 28px}
.search svg{position:absolute;left:8px;top:9px}
.main-nav{left:610px;top:72px;width:460px;display:flex;justify-content:space-between;color:var(--white);font-size:17px}

/* hero */
.hero{left:0;top:117px;width:1200px;height:561px;background:linear-gradient(90deg,#3a1410 0%,#5a2a1c 35%,#6e5a48 60%,#8a7a5e 80%,#4a3a2a 100%)}
.hero-title{left:612px;top:355px;font-size:82px;color:var(--white);letter-spacing:1px}
.hero-arrow{top:376px}

/* promo tiles */
.promo{top:707px;width:293px;height:239px;text-align:center;color:var(--white)}
.promo-1{left:131px;background:linear-gradient(135deg,#3a3a3a,#151515)}
.promo-2{left:453px;background:linear-gradient(135deg,#9a9a9a,#c9c2bb)}
.promo-3{left:776px;background:linear-gradient(135deg,#b31c1c,#e2d6d0)}
.promo-kicker{font-size:30px;margin-top:76px;line-height:1}
.promo-title{font-size:46px;line-height:1}
.divider{left:131px;width:938px;height:1px;background:var(--line)}

/* products */
.product{width:211px;height:251px;border:1px solid var(--card-line);background:var(--white)}
.product-img{left:0;top:0;width:209px;height:137px;border-bottom:1px solid var(--card-line);background:radial-gradient(circle at 55% 55%,#5d6a30 0 22%,#d8b07a 23% 30%,#fff 31%)}
.product-img.jar{background:radial-gradient(ellipse 16% 26% at 50% 55%,#d2a13a 0 90%,#fff 100%)}
.badge{left:0;top:0}
.product-title{left:8px;top:148px;font-size:14px;color:var(--text-dark);white-space:nowrap}
.product-title span{color:#888}
.product-meta{left:8px;top:172px;font-size:10.5px;line-height:19px;color:#555}
.price{color:var(--red-price);font-family:"Bebas Neue",Impact,sans-serif;font-size:14px}

/* side boxes */
.newsletter{left:846px;top:1005px;width:223px;height:204px;background:var(--gold);color:var(--white);padding:12px 16px}
.newsletter h3{font-size:27px;text-align:center;line-height:1;font-weight:400}
.newsletter p{font-size:11.5px;line-height:23px;margin-top:6px}
.newsletter .field{height:24px;background:var(--white);color:#aaa;font-size:10px;padding:6px;margin-top:10px}
.newsletter .btn{display:inline-block;background:#333;color:var(--white);font-size:14px;padding:5px 10px 2px;margin-top:16px}
.sale{left:846px;top:1238px;width:223px;height:296px;background:linear-gradient(#8a8f95,#b7b8bb 60%,#d8d2cf);color:var(--white);text-align:center}
.sale-big{left:0;top:38px;width:223px;font-size:66px;line-height:1}
.sale-sub{left:0;top:118px;width:223px;font-size:38px;line-height:1}
.sale-btn{left:40px;top:165px;width:144px;height:34px;border:2px solid var(--white);font-size:19px;padding-top:6px}
.sale-note{left:20px;top:240px;width:190px;font-size:11px;line-height:14px;text-align:left}

/* pagination */
.pager{left:343px;top:1568px;display:flex;gap:4px}
.pager span{width:18px;height:18px;border:1px solid #bbb;border-radius:50%;font-size:10px;text-align:center;line-height:16px;color:#333}
.pager .current{background:var(--red);border-color:var(--red);color:var(--white)}

/* about */
.about-title{left:131px;top:1638px;font-size:32px;color:var(--red)}
.about-text{left:131px;top:1687px;width:940px;font-size:15px;line-height:28px;color:#777}
.about-text p+p{margin-top:6px}

/* footer */
.site-footer{left:0;top:1859px;width:1200px;height:328px;background:radial-gradient(ellipse at 30% 40%,#2a2a2a,var(--footer) 70%)}
.col-title{top:1903px;font-size:20px;color:var(--white);font-weight:400}
.links{top:1937px;font-size:12px;line-height:24.5px;color:#ddd;list-style:none}
.links li::before{content:"›";font-weight:700;margin-right:9px}
.recent-thumb{left:131px;top:1942px;width:103px;height:111px;background:linear-gradient(90deg,#5b1a14,#2a1a16 50%,#6a5a4a)}
.recent-text{left:249px;top:1937px;width:215px;font-size:12px;line-height:19.6px;color:#ddd}
.social{left:534px;top:2103px;display:flex;gap:10px}
.social span{width:18px;height:18px;border-radius:50%;background:var(--white)}
.copyright{left:0;top:2144px;width:1200px;text-align:center;font-size:12px;color:#ddd}
</style>
</head>
<body>

<header class="site-header abs">
  <div class="brand abs">YUNTAO</div>
  <div class="search abs">
    <svg width="14" height="14" viewBox="0 0 14 14"><circle cx="9" cy="5" r="4" fill="none" stroke="#fff" stroke-width="1.6"/><line x1="6" y1="8" x2="1" y2="13" stroke="#fff" stroke-width="2"/></svg>
    Enter any Keywords....
  </div>
  <nav class="main-nav abs"><span>About YUNTAO</span><span>Collection</span><span>Tea House</span><span>Contact Us</span></nav>
</header>

<section class="hero abs" role="img" aria-label="Tea house interior with red lanterns, lounge seating and a lit stone corridor"></section>
<h1 class="hero-title abs display">Tea and Tea Sets</h1>
<svg class="hero-arrow abs" style="left:7px" width="46" height="46" viewBox="0 0 46 46"><circle cx="23" cy="23" r="21" fill="rgba(0,0,0,.35)" stroke="#fff" stroke-width="3"/><polyline points="26,14 17,23 26,32" fill="none" stroke="#fff" stroke-width="4"/></svg>
<svg class="hero-arrow abs" style="left:1145px" width="46" height="46" viewBox="0 0 46 46"><circle cx="23" cy="23" r="21" fill="rgba(0,0,0,.35)" stroke="#fff" stroke-width="3"/><polyline points="20,14 29,23 20,32" fill="none" stroke="#fff" stroke-width="4"/></svg>

<a class="promo promo-1 abs" role="img" aria-label="Terra cotta warrior figure">
  <div class="promo-kicker display" style="color:#c01818">Book a</div><div class="promo-title display">Consultation</div>
</a>
<a class="promo promo-2 abs" role="img" aria-label="Porcelain tea set with flower pattern">
  <div class="promo-kicker display" style="color:#39c12a">Today</div><div class="promo-title display">Register</div>
</a>
<a class="promo promo-3 abs" role="img" aria-label="Framed red paper-cut artwork">
  <div class="promo-kicker display" style="color:#f0a020">Get Advice</div><div class="promo-title display">Now!</div>
</a>

<div class="divider abs" style="top:972px"></div>

<article class="product abs" style="left:131px;top:1005px">
  <div class="product-img abs" role="img" aria-label="Green tea leaves on a wooden scoop"></div>
  <svg class="badge abs" width="58" height="58" viewBox="0 0 58 58"><polygon points="0,0 58,0 0,58" fill="#9b0d0d"/><text x="14" y="32" transform="rotate(-45 14 32)" fill="#fff" font-size="11" font-family="Bebas Neue,Impact,sans-serif">NEW</text></svg>
  <div class="product-title abs display">Tea and Tea Sets <span>Lorem ipsum dolor</span></div>
  <div class="product-meta abs">Origin : Yunnaga China<br>style : Endless layout and styling<br>Technique : Accessories to impress<br>Price : <span class="price">$890.00</span></div>
</article>
<article class="product abs" style="left:366px;top:1005px">
  <div class="product-img jar abs" role="img" aria-label="Painted porcelain tea jar"></div>
  <svg class="badge abs" width="58" height="58" viewBox="0 0 58 58"><polygon points="0,0 58,0 0,58" fill="#f4a300"/><text x="14" y="32" transform="rotate(-45 14 32)" fill="#fff" font-size="11" font-family="Bebas Neue,Impact,sans-serif">SALE</text></svg>
  <div class="product-title abs display">Tea and Tea Sets <span>Lorem ipsum dolor</span></div>
  <div class="product-meta abs">Origin : Yunnaga China<br>style : Endless layout and styling<br>Technique : Accessories to impress<br>Price : <span class="price">$890.00</span></div>
</article>
<article class="product abs" style="left:602px;top:1005px">
  <div class="product-img abs" role="img" aria-label="Green tea leaves on a wooden scoop"></div>
  <div class="product-title abs display">Tea and Tea Sets <span>Lorem ipsum dolor</span></div>
  <div class="product-meta abs">Origin : Yunnaga China<br>style : Endless layout and styling<br>Technique : Accessories to impress<br>Price : <span class="price">$890.00</span></div>
</article>
<article class="product abs" style="left:131px;top:1283px">
  <div class="product-img abs" role="img" aria-label="Green tea leaves on a wooden scoop"></div>
  <div class="product-title abs display">Tea and Tea Sets <span>Lorem ipsum dolor</span></div>
  <div class="product-meta abs">Origin : Yunnaga China<br>style : Endless layout and styling<br>Technique : Accessories to impress<br>Price : <span class="price">$890.00</span></div>
</article>
<article class="product abs" style="left:366px;top:1283px">
  <div class="product-img jar abs" role="img" aria-label="Painted porcelain tea jar"></div>
  <svg class="badge abs" width="58" height="58" viewBox="0 0 58 58"><polygon points="0,0 58,0 0,58" fill="#f4a300"/><text x="14" y="32" transform="rotate(-45 14 32)" fill="#fff" font-size="11" font-family="Bebas Neue,Impact,sans-serif">SALE</text></svg>
  <div class="product-title abs display">Tea and Tea Sets <span>Lorem ipsum dolor</span></div>
  <div class="product-meta abs">Origin : Yunnaga China<br>style : Endless layout and styling<br>Technique : Accessories to impress<br>Price : <span class="price">$890.00</span></div>
</article>
<article class="product abs" style="left:602px;top:1283px">
  <div class="product-img abs" role="img" aria-label="Green tea leaves on a wooden scoop"></div>
  <div class="product-title abs display">Tea and Tea Sets <span>Lorem ipsum dolor</span></div>
  <div class="product-meta abs">Origin : Yunnaga China<br>style : Endless layout and styling<br>Technique : Accessories to impress<br>Price : <span class="price">$890.00</span></div>
</article>

<aside class="newsletter abs">
  <h3 class="display">Sign up Newsletter</h3>
  <p>Want to be the know? Sign up for one or all of our Newsletter!</p>
  <div class="field">Mail:</div>
  <span class="btn display">Sign up now</span>
</aside>

<aside class="sale abs" role="img" aria-label="Porcelain tea cups and flowers on a table">
  <div class="sale-big abs display">Sale</div>
  <div class="sale-sub abs display">Upto 50% Save</div>
  <div class="sale-btn abs display">Shop Now!</div>
  <div class="sale-note abs display">Lorem ipsum is simply dummy text of the and typesetting industry ..............</div>
</aside>

<nav class="pager abs">
  <span>&lt;&lt;</span><span>1</span><span class="current">2</span><span>3</span><span>4</span><span>5</span><span>6</span><span>7</span><span>8</span><span>9</span><span>10</span><span>&gt;&gt;</span>
</nav>

<div class="divider abs" style="top:1611px;left:124px;width:946px"></div>

<h2 class="about-title abs display">About Us</h2>
<div class="about-text abs">
  <p>Yun meaning cloud, is the symbolic image from the mythical orient. Tao has a literal meaning of pottery, connoting craft and refinement in traditional Chinese culture.&nbsp; At Yuntao, we present you the authentic oriental cultural experience through a rich collection of traditional Chinese artwork and artifact with premium quality and finishing.&nbsp; ..............</p>
  <p>At Yuntao, we handpick the highest grade tea from China to bring you to the amorous and tranquil world of Chinese tea garden.&nbsp; At Yuntao, we await you.</p>
</div>

<footer class="site-footer abs"></footer>
<h4 class="col-title abs" style="left:131px">Recent Products</h4>
<div class="recent-thumb abs" role="img" aria-label="Tea house lounge interior"></div>
<p class="recent-text abs">Sed ut perspiciatis unde omnis iste natus error sit voluptatem accusantium doloremque laudantium, totam rem aperiam, eaque nisi ut aliquid ex ea commodi<br>Read More</p>

<h4 class="col-title abs" style="left:502px">Quick Links</h4>
<ul class="links abs" style="left:502px"><li>lorem ipsum dolorsit</li><li>lorem ipsum dolorsit</li><li>Sign-up List</li><li>Write for Brands</li><li>Our Archives</li></ul>

<h4 class="col-title abs" style="left:717px">Information</h4>
<ul class="links abs" style="left:717px"><li>Tea and Tea Sets</li><li>Tea and Tea Sets</li><li>Porcelain Flower Tea Pot</li><li>Porcelain Flower Tea Pot</li><li>Porcelain Flower Tea Pot</li></ul>

<h4 class="col-title abs" style="left:933px">Collection</h4>
<ul class="links abs" style="left:933px"><li>Porcelain</li><li>Bronze</li><li>Painting &amp; Calligraphy</li><li>Terra Cotta</li><li>Others</li></ul>

<div class="social abs" aria-label="Social links"><span></span><span></span><span></span><span></span><span></span></div>
<p class="copyright abs">Copyright © 2014 All Rights Reserved.</p>

</body>
</html>
```